Bi-fold brochure/business card for Restoration company
Marketing brochure and Business card
Bi-fold brochure/business card for Restoration company - Construction
Creative Brief
Construction
Insurance adjusters, property management cos, home owners, plumbers, roofers, builders etc.
(Need a bi-fold brochure, simple, elegant and classic) (logo is draft #135) Page#1: When unexpected happens…., expect…. Logo & Company Name Complete Restoration & Reconstruction services Water Damage  Sewer Backup  Mold  Fire & Smoke Residential  Commercial  Institutional (kind of footnotes with small font compared to rest of the font in this page) (Have the logo of BTFQN and KDW in the corner somewhere in the first page) Page #2: Key Features: • BTFQN Certified Firm • Professionally Managed Company (KDW® certified) • Excellence, Ethical and Reliable • Prompt and Competitive Estimates • Committed to Response within 60 minutes • Highest Priority for Health & Safety • Green & Eco-friendly • Exceptional Customer care • Cutting Edge, Tested & Approved Restoration Process • High Quality and Latest Equipments • 24x7 Dedicated & Prompt service (Some pictures of water/mold/fire/smoke/sewage in Page 2 & 3. If you can find any suitable pictures can use it and I am also working on the pictures) Page #3: Capabilities: • Water Damage Remediation • Sewer Backup Remediation • Mold Inspection & Remediation • Fire/Smoke Damage Remediation • Structural Drying • Security Board-up • Content Pack-out & Cleaning • Odor Removal & Control • Carpet Cleaning • Complete Reconstruction o Drywall and Insulation o Roofing o Flooring o Painting Page #4: Company name with Logo, www.qualmend.ca & ph no: 403-771-4286 (half the page) (rest half of the page have the below 4 items in some box type with pictures and text embossed on top of pict) Water (inside a box and the text on top of a picture representing water) Mold (inside a box and the text on top of a picture representing mold, something like http://www.brelvinhome.com/is-this-mold) Fire/Smoke (inside a box and the text on top of a picture representing Fire or/and smoke) Reconstruction (inside a box and the text on top of a picture representing reconstruction)

```html
<!DOCTYPE html>
<html lang="en">
<head>
<meta charset="utf-8">
<title>Qualmend Brochure and Business Card</title>
<link href="https://fonts.googleapis.com/css2?family=Open+Sans:wght@400;600;700;800&display=swap" rel="stylesheet">
<style>
:root{
  --bg:#e9e6e1;
  --dark:#1f2024;
  --dark-2:#2c2e33;
  --green:#7cc142;
  --green-deep:#4f9a2a;
  --blue:#1b5fb3;
  --blue-deep:#0f3f86;
  --white:#ffffff;
  --ink:#2a2a2a;
  --muted:#9aa0a6;
  --water:#6f9ec4;
  --mold:#8c8a6e;
  --fire:#d9772f;
  --build:#a89c86;
  --sand:#d8c6a6;
  --house:#9cb8dc;
  --worker:#c8a36a;
}
*{box-sizing:border-box;margin:0;padding:0}
html,body{width:1200px;height:892px;overflow:hidden}
body{background:var(--bg);font-family:"Open Sans",Arial,sans-serif;color:var(--ink);position:relative}
.piece{position:absolute;overflow:hidden;box-shadow:0 3px 10px rgba(0,0,0,.28)}
.panel{position:absolute;top:0;bottom:0;overflow:hidden}
.curves{position:absolute;inset:0;width:100%;height:100%}
.photo{position:absolute;border:2px solid var(--white)}
.photo .tag{position:absolute;left:6px;bottom:4px;color:var(--white);font-weight:700;font-size:12px;text-shadow:0 1px 2px rgba(0,0,0,.6)}
.photo.water{background:linear-gradient(160deg,#a9c6de,var(--water))}
.photo.mold{background:linear-gradient(160deg,#b6b39a,var(--mold))}
.photo.fire{background:linear-gradient(160deg,#f0b266,var(--fire) 55%,#6b4a3a)}
.photo.build{background:linear-gradient(160deg,#d3c8b2,var(--build))}
.brand{position:absolute;display:flex;align-items:center;gap:6px;font-weight:700;color:var(--blue)}
.brand .dot{width:14px;height:14px;border-radius:50%;background:var(--green);flex:none}
.brand.on-dark{color:var(--white)}
.headline{position:absolute;color:var(--white);font-weight:800;line-height:1.15}
.small{position:absolute;font-size:8px;line-height:1.35}
.sectors{position:absolute;list-style:none;font-size:8px;font-weight:700;color:var(--white);line-height:1.45}
.sectors li::before{content:"";display:inline-block;width:5px;height:5px;background:var(--green);margin-right:4px}
.list{position:absolute;list-style:none;color:var(--white);font-size:10.5px;line-height:1.62}
.list li::before{content:"";display:inline-block;width:5px;height:5px;border-radius:50%;background:var(--green);margin-right:6px;vertical-align:middle}
.list li.sub{padding-left:16px;font-size:9.5px}
.list li.sub::before{background:none;border:1px solid var(--white)}
.heading{position:absolute;color:var(--white);font-weight:800;font-size:19px;display:flex;align-items:center;gap:8px}
.tick{width:20px;height:20px}
.badge{position:absolute;width:26px;height:26px;border-radius:4px}
</style>
</head>
<body>

<!-- Outside spread, version A -->
<section class="piece" style="left:29px;top:65px;width:554px;height:290px;">
  <div class="panel" style="left:0;width:277px;background:var(--white);">
    <svg class="curves" viewBox="0 0 277 290" preserveAspectRatio="none">
      <path d="M0 0 H70 C20 80 20 200 110 290 H0 Z" fill="var(--blue)"/>
      <path d="M60 0 C15 90 30 210 130 290 H110 C20 200 20 80 70 0 Z" fill="var(--green)"/>
      <path d="M170 290 C230 250 260 200 277 150 V290 Z" fill="var(--green)" opacity=".9"/>
    </svg>
    <div class="photo water" role="img" aria-label="Photo of a flooded room" style="left:14px;top:12px;width:110px;height:58px"><span class="tag">Water</span></div>
    <div class="photo mold" role="img" aria-label="Photo of mold on a wall" style="left:14px;top:78px;width:110px;height:58px"><span class="tag">Mold</span></div>
    <div class="photo fire" role="img" aria-label="Photo of a house fire" style="left:14px;top:144px;width:110px;height:58px"><span class="tag">Fire/Smoke</span></div>
    <div class="photo build" role="img" aria-label="Photo of reconstruction work" style="left:132px;top:144px;width:110px;height:58px"><span class="tag">Reconstruction</span></div>
    <div class="brand" style="left:120px;top:222px;font-size:20px"><span class="dot"></span>qualmend</div>
    <p class="small" style="left:124px;top:252px;color:var(--ink)">www.qualmend.ca<br>Cell: 403-771-4286</p>
  </div>
  <div class="panel" style="left:277px;width:277px;background:var(--dark);">
    <svg class="curves" viewBox="0 0 277 290" preserveAspectRatio="none">
      <path d="M0 0 H40 C-10 100 20 200 120 290 H0 Z" fill="var(--green)"/>
      <path d="M0 0 H22 C-20 100 0 200 90 290 H0 Z" fill="var(--green-deep)"/>
    </svg>
    <div role="img" aria-label="Photo of a house drawn in sand" style="position:absolute;left:150px;top:0;width:127px;height:125px;background:linear-gradient(150deg,#eadcc2,var(--sand))"></div>
    <ul class="sectors" style="left:100px;top:14px">
      <li>Residential</li><li>Commercial</li><li>Institutional</li>
    </ul>
    <p class="headline" style="left:92px;top:132px;font-size:18px">When<br>unexpected<br>happens…,<br>expect…</p>
    <div class="brand on-dark" style="left:92px;top:222px;font-size:18px"><span class="dot"></span>qualmend</div>
    <p class="small" style="left:92px;top:250px;color:var(--white);font-size:7px">Complete Restoration &amp; Reconstruction Services<br>Water Damage • Sewer Backup • Mold • Fire &amp; Smoke</p>
  </div>
</section>

<!-- Outside spread, version B -->
<section class="piece" style="left:600px;top:65px;width:569px;height:290px;">
  <div class="panel" style="left:0;width:284px;background:var(--white);">
    <svg class="curves" viewBox="0 0 284 290" preserveAspectRatio="none">
      <path d="M0 200 C90 160 200 170 284 230 V290 H0 Z" fill="var(--green)"/>
      <path d="M0 230 C100 190 200 200 284 260 V290 H0 Z" fill="var(--blue)"/>
      <path d="M0 250 C100 215 200 225 284 280 V290 H0 Z" fill="var(--dark)"/>
    </svg>
    <div class="photo water" role="img" aria-label="Photo of water damage" style="left:8px;top:8px;width:128px;height:72px"><span class="tag">Water</span></div>
    <div class="photo mold" role="img" aria-label="Photo of mold growth" style="left:142px;top:8px;width:128px;height:72px"><span class="tag">Mold</span></div>
    <div class="photo fire" role="img" aria-label="Photo of fire and smoke" style="left:8px;top:86px;width:128px;height:72px"><span class="tag">Fire/Smoke</span></div>
    <div class="photo build" role="img" aria-label="Photo of a reconstruction site" style="left:142px;top:86px;width:128px;height:72px"><span class="tag">Reconstruction</span></div>
    <div class="brand on-dark" style="left:64px;top:236px;font-size:20px"><span class="dot"></span>qualmend</div>
    <p class="small" style="left:190px;top:224px;color:var(--white);font-weight:600">www.qualmend.ca<br>Cell: 403-771-4286</p>
  </div>
  <div class="panel" style="left:284px;width:285px;background:var(--dark);">
    <div role="img" aria-label="Photo of a small blue house model on a white surface" style="position:absolute;left:0;top:0;width:285px;height:135px;background:radial-gradient(circle at 55% 45%,var(--house),#d9dee6 60%)"></div>
    <svg class="curves" viewBox="0 0 285 290" preserveAspectRatio="none">
      <path d="M0 120 C100 150 200 120 285 90 V140 C200 160 100 185 0 170 Z" fill="var(--green)"/>
      <path d="M0 170 C100 185 200 160 285 140 V150 C200 175 100 195 0 180 Z" fill="var(--blue)"/>
    </svg>
    <p class="headline" style="left:14px;top:186px;font-size:18px">When unexpected<br>happens…, expect…</p>
    <div class="brand on-dark" style="left:14px;top:238px;font-size:18px"><span class="dot"></span>qualmend</div>
    <p class="small" style="left:14px;top:264px;color:var(--white);font-size:7px">Complete Restoration &amp; Reconstruction Services<br>Water Damage • Sewer Backup • Mold • Fire &amp; Smoke</p>
    <ul class="sectors" style="left:200px;top:196px">
      <li>Residential</li><li>Commercial</li><li>Institutional</li>
    </ul>
  </div>
</section>

<!-- Inside spread -->
<section class="piece" style="left:29px;top:384px;width:631px;height:480px;">
  <div class="panel" style="left:0;width:315px;background:var(--dark);">
    <svg class="curves" viewBox="0 0 315 480" preserveAspectRatio="none">
      <path d="M0 0 H315 V18 C200 10 80 30 0 70 Z" fill="var(--dark-2)"/>
      <path d="M0 360 C100 330 220 360 315 420 V440 C220 385 100 355 0 385 Z" fill="var(--green)"/>
    </svg>
    <div class="heading" style="left:16px;top:32px">
      <svg class="tick" viewBox="0 0 20 20"><path d="M2 10 L8 16 L18 3" fill="none" stroke="var(--green)" stroke-width="3.5"/></svg>
      Key Features:
    </div>
    <span class="badge" style="left:246px;top:28px;background:var(--white)"></span>
    <span class="badge" style="left:278px;top:28px;background:var(--green);border-radius:50%"></span>
    <ul class="list" style="left:20px;top:72px">
      <li>BTFQN Certified Firm</li>
      <li>Professionally Managed Company (KDW® certified)</li>
      <li>Excellence, Ethical and Reliable</li>
      <li>Prompt and Competitive Estimates</li>
      <li>Committed to Response within 60 minutes</li>
      <li>Highest Priority for Health &amp; Safety</li>
      <li>Green &amp; Eco-friendly</li>
      <li>Exceptional Customer care</li>
      <li>Cutting Edge, Tested &amp; Approved Restoration Process</li>
      <li>High Quality and Latest Equipments</li>
      <li>24x7 Dedicated &amp; Prompt service</li>
    </ul>
    <div class="photo build" role="img" aria-label="Photo of reconstruction work" style="left:0;top:396px;width:158px;height:84px;border-width:2px 1px 0 0"><span class="tag">Reconstruction</span></div>
    <div class="photo fire" role="img" aria-label="Photo of fire and smoke damage" style="left:158px;top:396px;width:157px;height:84px;border-width:2px 1px 0 1px"><span class="tag">Fire/Smoke</span></div>
  </div>
  <div class="panel" style="left:315px;width:316px;background:linear-gradient(160deg,#9ad25f,var(--green) 45%,var(--green-deep));">
    <svg class="curves" viewBox="0 0 316 480" preserveAspectRatio="none">
      <path d="M0 300 C60 380 180 400 316 380 V400 C180 420 60 400 0 330 Z" fill="var(--blue)"/>
    </svg>
    <div class="heading" style="left:16px;top:18px">
      <svg class="tick" viewBox="0 0 20 20"><path d="M2 10 L8 16 L18 3" fill="none" stroke="var(--white)" stroke-width="3.5"/></svg>
      Capabilities:
    </div>
    <ul class="list" style="left:20px;top:52px;font-size:9.5px;line-height:1.55">
      <li>Water Damage Remediation</li>
      <li>Sewer Backup Remediation</li>
      <li>Mold Inspection &amp; Remediation</li>
      <li>Fire/Smoke Damage Remediation</li>
      <li>Structural Drying</li>
      <li>Security Board-up</li>
      <li>Content Pack-out &amp; Cleaning</li>
      <li>Odor Removal &amp; Control</li>
      <li>Carpet Cleaning</li>
      <li>Complete Reconstruction</li>
      <li class="sub">Drywall and Insulation</li>
      <li class="sub">Roofing</li>
      <li class="sub">Flooring</li>
      <li class="sub">Painting</li>
    </ul>
    <div role="img" aria-label="Photo of a construction worker holding a clipboard" style="position:absolute;left:188px;top:140px;width:118px;height:190px;border-radius:6px;background:linear-gradient(180deg,#e9c23a 0 12%,#d9d3c3 12% 45%,var(--worker) 45% 100%)"></div>
    <div class="photo mold" role="img" aria-label="Photo of mold" style="left:0;top:396px;width:158px;height:84px;border-width:2px 1px 0 1px"><span class="tag">Mold</span></div>
    <div class="photo water" role="img" aria-label="Photo of water damage" style="left:158px;top:396px;width:158px;height:84px;border-width:2px 0 0 1px"><span class="tag" style="left:auto;right:8px">Water</span></div>
  </div>
</section>

<!-- Business card front -->
<section class="piece" style="left:672px;top:516px;width:456px;height:144px;background:var(--white);">
  <svg class="curves" viewBox="0 0 456 144" preserveAspectRatio="none">
    <path d="M0 0 H90 C40 40 40 100 110 144 H0 Z" fill="var(--blue)"/>
    <path d="M80 0 H96 C44 40 46 100 122 144 H104 C34 100 32 40 80 0 Z" fill="var(--green)"/>
  </svg>
  <div class="brand" style="left:64px;top:56px;font-size:24px"><span class="dot"></span>qualmend</div>
  <p style="position:absolute;left:250px;top:24px;font-weight:700;font-size:13px;color:var(--ink)">Daniel Forsyth</p>
  <p class="small" style="left:250px;top:42px;color:var(--muted)">Project Manager</p>
  <p class="small" style="left:250px;top:70px;color:var(--ink)">125 Ridge Lane<br>Calgary, AB T2P 1K4<br>Ph: 403-771-4286<br>www.qualmend.ca</p>
</section>

<!-- Business card back -->
<section class="piece" style="left:672px;top:712px;width:456px;height:164px;background:var(--dark);">
  <svg class="curves" viewBox="0 0 456 164" preserveAspectRatio="none">
    <path d="M0 20 C150 0 320 10 456 40 V46 C320 18 150 8 0 28 Z" fill="var(--green)" opacity=".6"/>
  </svg>
  <p style="position:absolute;left:0;right:0;top:26px;text-align:center;color:var(--white);font-size:11px;font-weight:600">Complete Restoration &amp; Reconstruction Services</p>
  <div class="brand on-dark" style="left:160px;top:62px;font-size:26px"><span class="dot"></span>qualmend</div>
  <p style="position:absolute;left:0;right:0;top:128px;text-align:center;color:var(--white);font-size:10px">Water Damage • Sewer Backup • Mold • Fire &amp; Smoke</p>
</section>

</body>
</html>
```